"Lanterns Along Every Quiet Road" Sermon Series Design

Needing a design for our church's next sermon series titled "Lanterns Along Every Quiet Road" where we will discuss the need for unity, diversity, love and clarity. Looking for a 1920 x 1080 (or higher res) editable and layered file (PSD or AI) so that we can reformat the design to work on social, screens, lower thirds and various print and online mediums. We will also need to have access to the font files so that we can make resize and tweak as needed. We like the idea of using a globe or map of the world as the backdrop with the words overtop. Or, the idea of creating a bunch of newspaper clippings (generic, so that they can't actually be read) and making the shape of a heart. See attached examples. This website will give you an idea of our previous sermon series designs so you can have an idea of our style (but, feel free to help us advance the ball on something more aligned with current design trends): https://www.brambleford.example/series

Examples use red, but stay away from a ton of red. If you're gonna major in a color, use blue or something in that family.

Must haves:
Title: Lanterns Along Every Quiet Road
Tagline : (TBD - use some Lorem Ipsum as a placeholder and we will fill in later)
Our Logo (attached) (small towards bottom is standard - only use solid colors for logo - preferably just solid black or white)

Industry/Entity Type

Church

Font styles to use
Serif
Sans Serif

Requirements
Must have
• Title: Lanterns Along Every Quiet Road
Nice to have
• We like the idea of using a globe or map of the world as the backdrop with the words overtop. Or, the idea of creating a bunch of newspaper clippings (generic, so that they can't actually be read) and making the shape of a heart. See attached examples.

If you're gonna major on a color, stick with blue or something close.
Should not have
• Don't use red as the primary color (example we sent has red, but stay away from it)

```html
<!DOCTYPE html>
<html lang="en">
<head>
<meta charset="utf-8">
<title>Lanterns Along Every Quiet Road</title>
<link href="https://fonts.googleapis.com/css2?family=Bebas+Neue&display=swap" rel="stylesheet">
<style>
  :root {
    --space: #020202;
    --glow-core: #fff2b8;
    --glow-amber: #e8961a;
    --glow-rust: #7a3405;
    --ground-gold: #4a3f1c;
    --ground-deep: #0c161e;
    --title-orange: #c7650a;
    --title-gold: #f3d21a;
    --title-bronze: #a8580a;
    --tagline: #ffffff;
  }
  html, body {
    margin: 0;
    padding: 0;
    width: 1200px;
    height: 675px;
    overflow: hidden;
    background: var(--space);
  }
  .series-art {
    position: relative;
    width: 1200px;
    height: 675px;
    overflow: hidden;
    background: var(--space);
    font-family: "Bebas Neue", "Arial Narrow", sans-serif;
  }
  .horizon-backdrop {
    position: absolute;
    inset: 0;
    background:
      radial-gradient(circle at 255px 455px, var(--glow-core) 0, var(--glow-amber) 70px, rgba(122,52,5,0.75) 260px, rgba(2,2,2,0) 560px),
      linear-gradient(180deg, rgba(2,2,2,0) 62%, rgba(20,26,30,0.6) 78%, rgba(12,22,30,0.9) 100%),
      linear-gradient(90deg, var(--ground-gold) 0%, var(--space) 50%, var(--ground-deep) 100%);
    background-blend-mode: normal;
  }
  .series-title {
    margin: 0;
    font-weight: 400;
    text-transform: uppercase;
  }
  .series-title span {
    position: absolute;
    left: 354px;
    width: 446px;
    line-height: 1;
    white-space: nowrap;
    background-clip: text;
    -webkit-background-clip: text;
    color: transparent;
    filter: drop-shadow(3px 5px 5px rgba(0,0,0,0.75));
  }
  .title-lead {
    top: 206px;
    font-size: 70px;
    background-image: linear-gradient(180deg, var(--title-orange), #b4560a);
  }
  .title-key {
    top: 237px;
    font-size: 217px;
    letter-spacing: 1px;
    background-image: linear-gradient(35deg, var(--title-gold) 0%, #e5a413 40%, var(--title-bronze) 85%);
  }
  .title-tail {
    top: 420px;
    font-size: 63px;
    text-align: right;
    background-image: linear-gradient(180deg, #e9c81c, #c9a010);
  }
  .tagline {
    position: absolute;
    left: 0;
    right: 0;
    top: 549px;
    margin: 0;
    line-height: 1;
    text-align: center;
    color: var(--tagline);
    font-size: 38px;
    letter-spacing: 0.3px;
    text-transform: uppercase;
    text-shadow: 2px 3px 5px rgba(0,0,0,0.8);
  }
  .church-mark {
    position: absolute;
    left: 0;
    right: 0;
    bottom: 22px;
    display: flex;
    justify-content: center;
    align-items: center;
    gap: 8px;
    color: var(--tagline);
    font-size: 22px;
    letter-spacing: 2px;
    line-height: 1;
    text-transform: uppercase;
  }
  .church-mark-dot {
    width: 12px;
    height: 12px;
    border-radius: 50%;
    background: var(--tagline);
  }
</style>
</head>
<body>
  <main class="series-art">
    <div class="horizon-backdrop" role="img" aria-label="Photograph of the Earth's curved horizon from space with the sun rising on the left"></div>

    <h1 class="series-title">
      <span class="title-lead">Lanterns Along</span>
      <span class="title-key">Every</span>
      <span class="title-tail">Quiet Road</span>
    </h1>

    <p class="tagline">"Lorem ipsum dolor sit amet, consectetur adipiscing elit,</p>

    <div class="church-mark"><span class="church-mark-dot"></span><span>Brambleford</span></div>
  </main>
</body>
</html>
```